sydney wedding photography business needs a business card design

we need a business card design for a sydney based wedding photography and videography business. our business name is :golden hour photography and video. our target clients are 24-35 yrs female. our style is candid, organic, natural, dynamic. we are a team of young photographers and videographers, and help brides to create memories that they will cherish for the rest of their lives. the logo will be provided. we want an elegant design that reflects our style, and also want to give a great impression to our clients that we are one of the best studios in sydney and our brand means quality and premium service.

Target Market(s)

bride to be, 24-35 years old, living in sydney and surrunding areas

Industry/Entity Type

Wedding Photography

Contact Information for Business Card

address: 57 marrow lane, bexton nsw 2041
mobile: 0431872056
phone: (02) 9361 2748
info@goldenhourstudio.net.au
www.goldenhourstudio.net.au
facebook:goldenhourbridals
instagram:goldenhourbridals

Font styles to use
Serif
Sans Serif

Requirements
Nice to have
• maybe add my slogan"Moments That Last Forever" if the layout looks good
Should not have
• no black color, not good idea for wedding biz card

```html
<!DOCTYPE html>
<html lang="en">
<head>
<meta charset="utf-8">
<title>Golden Hour Photography and Video – Business Card</title>
<link rel="stylesheet" href="https://fonts.googleapis.com/css2?family=Cormorant+Garamond:wght@500&family=Montserrat:wght@400&display=swap">
<style>
  :root {
    --canvas: #ecebe8;
    --card: #fbfaf7;
    --gold: #ad8c4e;
    --gold-light: #e4d3a8;
    --gold-pale: #f3ead3;
    --shadow: rgba(120, 100, 60, 0.18);
  }
  * { box-sizing: border-box; margin: 0; padding: 0; }
  html, body {
    width: 1200px; height: 1000px; overflow: hidden;
    background: var(--canvas);
  }
  .sheet {
    width: 1200px; height: 1000px;
    display: flex; flex-direction: column; align-items: center; justify-content: center;
    gap: 48px;
  }
  .card {
    position: relative;
    width: 700px; height: 428px;
    background: var(--card);
    box-shadow: 0 8px 24px var(--shadow);
    overflow: hidden;
    color: var(--gold);
  }
  .ornament { position: absolute; left: 0; width: 100%; display: block; }
  .ornament--front { top: 0; height: 215px; }
  .ornament--back-top { top: 0; height: 90px; }
  .ornament--back-bottom { bottom: 0; height: 90px; }

  /* front */
  .brand {
    position: absolute; left: 0; right: 0; top: 228px;
    text-align: center;
  }
  .brand__name {
    font-family: "Cormorant Garamond", serif;
    font-weight: 500; font-size: 50px; line-height: 1;
    color: var(--gold);
  }
  .brand__sub {
    margin-top: 8px;
    font-family: "Montserrat", sans-serif;
    font-size: 12px; letter-spacing: 0.62em;
    text-transform: uppercase; padding-left: 0.62em;
  }
  .slogan {
    position: absolute; left: 40px; right: 40px; top: 340px;
    display: flex; align-items: center; gap: 18px;
  }
  .slogan__rule { flex: 1; height: 1px; background: var(--gold); }
  .slogan__text {
    font-family: "Cormorant Garamond", serif;
    font-weight: 500; font-size: 17px; letter-spacing: 0.1em;
    text-transform: uppercase; white-space: nowrap;
  }

  /* back */
  .brand--small { top: 104px; }
  .brand--small .brand__name { font-size: 26px; }
  .brand--small .brand__sub { font-size: 8px; margin-top: 4px; }
  .contact {
    position: absolute; left: 0; right: 0; top: 170px;
    display: flex; justify-content: center; align-items: stretch;
    font-family: "Cormorant Garamond", serif; font-weight: 500;
    font-size: 16px; line-height: 1.6;
    white-space: nowrap;
  }
  .contact__column { padding: 0 22px; }
  .contact__column--left { text-align: right; }
  .contact__divider { width: 1px; background: var(--gold); }
  .contact__address {
    position: absolute; left: 0; right: 0; top: 266px;
    text-align: center;
    font-family: "Cormorant Garamond", serif; font-weight: 500; font-size: 16px;
  }
</style>
</head>
<body>
<main class="sheet">

  <section class="card card--front" aria-label="Card front">
    <svg class="ornament ornament--front" viewBox="0 0 700 215" preserveAspectRatio="none" role="img" aria-label="Gold henna-style floral and paisley ornament band">
      <defs>
        <linearGradient id="ornamentFront" x1="0" y1="0" x2="1" y2="1">
          <stop offset="0" stop-color="#d9c28c"/>
          <stop offset="0.5" stop-color="#efe2bf"/>
          <stop offset="1" stop-color="#d6bd83"/>
        </linearGradient>
      </defs>
      <path d="M0 0 H700 V120 C620 170 560 120 480 160 C400 200 320 150 240 190 C160 225 80 180 0 210 Z" fill="url(#ornamentFront)"/>
    </svg>
    <div class="brand">
      <p class="brand__name">Golden Hour</p>
      <p class="brand__sub">Photography</p>
    </div>
    <div class="slogan">
      <span class="slogan__rule"></span>
      <span class="slogan__text">Moments That Last Forever</span>
      <span class="slogan__rule"></span>
    </div>
  </section>

  <section class="card card--back" aria-label="Card back">
    <svg class="ornament ornament--back-top" viewBox="0 0 700 90" preserveAspectRatio="none" role="img" aria-label="Gold floral ornament border">
      <defs>
        <linearGradient id="ornamentBack" x1="0" y1="0" x2="1" y2="0">
          <stop offset="0" stop-color="#efe2bf"/>
          <stop offset="1" stop-color="#d9c28c"/>
        </linearGradient>
      </defs>
      <path d="M260 0 H700 V85 C620 60 560 90 480 55 C400 20 330 40 260 0 Z" fill="url(#ornamentBack)"/>
    </svg>
    <div class="brand brand--small">
      <p class="brand__name">Golden Hour</p>
      <p class="brand__sub">Photography</p>
    </div>
    <div class="contact">
      <div class="contact__column contact__column--left">
        <p>P: (02) 9361 2748</p>
        <p>W: www.goldenhourstudio.net.au</p>
        <p>facebook: goldenhourbridals</p>
      </div>
      <span class="contact__divider"></span>
      <div class="contact__column contact__column--right">
        <p>M: 0431872056</p>
        <p>E: info@goldenhourstudio.net.au</p>
        <p>instagram: goldenhourbridals</p>
      </div>
    </div>
    <p class="contact__address">57 marrow lane, bexton nsw 2041</p>
    <svg class="ornament ornament--back-bottom" viewBox="0 0 700 90" preserveAspectRatio="none" role="img" aria-label="Gold floral ornament border">
      <defs>
        <linearGradient id="ornamentBackLow" x1="0" y1="0" x2="1" y2="0">
          <stop offset="0" stop-color="#d9c28c"/>
          <stop offset="1" stop-color="#efe2bf"/>
        </linearGradient>
      </defs>
      <path d="M0 15 C80 35 150 10 230 42 C310 72 380 55 470 90 H0 Z" fill="url(#ornamentBackLow)"/>
    </svg>
  </section>

</main>
</body>
</html>
```